We have 'joined together' 6 micro-sites with a common theme. Looking to upgrade the design of a total of 26 pages on the abovementioned sites, whilst maintaining a common look and feel.

Goal is to improve customer experience and conversion rate, whilst maintaining Quenbo rankings. New design to be responsive to different devices and SEO optimised

We prefer simple designs with the cleaness of Zorvane.com, however with more descriptive text. Target audience are business managers and owners, so site should convey professional capability, with a hint of playfulness. After all data can be fun? No?

See attached doc for further details.

Update: 19/8/2014. Following further consideration, the HTML coding no longer required. Once design is finalised, we require a PSD file for each page showing the full page layout, including all images and icons. We will extract the relevant bits from the PSD and do the coding and css inhouse.
Updates

Hi All The Mirel Group - PSD Design Only. HTML no longer required Following further consideration, the HTML / Css coding aspect of the project NO longer required. Once design is finalised, we require a PSD file from you for each of the 26 web pages, showing the page layout and including all images and icons. If one page layout is the same as another, then we request that you just supply images and icons for that page in a PSD file. We will then extract the relevant bits from the PSD and we will do the coding and css inhouse. Our main aim is to get an awesome, blow-your-sox-off design that compels users to convert. Many thanks in anticipation Oliver.

Project Deadline Extended
Reason: Changed deliverables from PSD, HTML and Coding t o PSD only. Hopefully this change will allow previous designers who were not interested to reconsider. Many thanks Oliver

Target Market(s)

Target market is business & IT managers within Australian organisations who are having problems with their data. Site must convey the impression that we are:
1) Very capable
2) Professional in our dealings
3) Reliable & trustworthy
4) Just a little bit quirky

Aprox. 60% of users are female, 40% male. Typically in the 30 to 55 year old bracket.

Number 1 requirements is that we don't embarrass our clients in any way.
2nd is that we do a good high quality job, delivering a good result.

We are not the cheapest nor the most expensive data shop around. We offer good value-for-money solutions. We are also reliable, friendly and available

Industry/Entity Type

Business

Font styles to use
Sans Serif

Requirements
Must have
• Simple yet information dense design. The "who we are" and "what we do" to be immediately visible above the fold. Images to be high quality. Good usability.
Simple navigation structure. Easy for users to find the info that they want.

In summary a simple, but good looking site, that compels users to contact us
Should not have
• No flash, fancy automation, rotating images, pop-ups etc.

```html
<!DOCTYPE html>
<html lang="en">
<head>
<meta charset="utf-8">
<title>The Mirel Group</title>
<link href="https://fonts.googleapis.com/css2?family=Arimo:ital,wght@0,400;0,700;1,400&family=Varela+Round&display=swap" rel="stylesheet">
<style>
:root{
  --orange:#ff6a00;
  --ink:#3a3a3a;
  --text:#444;
  --nav:#4b4b4b;
  --light:#f5f5f5;
  --card:#cbcbcb;
  --card-head:#4e4e4e;
  --footer:#454545;
  --footer-deep:#2f2f2f;
  --field:#6a6a6a;
  --quote-mark:#bbb;
}
*{margin:0;padding:0;box-sizing:border-box}
html,body{width:681px;height:1200px;overflow:hidden}
body{font-family:"Arimo",Arial,sans-serif;color:var(--text);background:#fff;position:relative}
.section{position:absolute;left:0;width:681px}
.header{top:0;height:64px}
.brand{position:absolute;left:38px;top:17px;display:flex;align-items:center;gap:9px;font:700 27px/1 "Arimo",sans-serif;color:var(--ink)}
.brand-square{width:20px;height:20px;background:var(--orange)}
.call{position:absolute;right:45px;top:19px;display:flex;align-items:center;gap:6px;color:#222}
.call small{display:block;font-size:9.5px}
.call strong{display:block;font-size:13.5px;font-weight:700}
.nav{top:64px;height:25px;background:var(--nav);display:flex;padding-left:38px}
.nav a{color:#fff;font-size:9px;text-decoration:none;line-height:25px;padding:0 10px}
.nav a.active{background:var(--orange);font-weight:700;padding:0 12px}
.hero{top:89px;height:221px;background:linear-gradient(90deg,#e9dcbf 0%,#e5d6b5 50%,#d8c7a0 100%)}
.hero-photo{position:absolute;left:280px;top:0;width:401px;height:221px;background:linear-gradient(180deg,#e7d8b6 0%,#cdb48a 80%,#8a6a4c 100%)}
.hero h1{position:absolute;left:43px;top:50px;font:400 26px/30px "Varela Round",sans-serif;color:var(--ink)}
.hero h1 span{color:var(--orange)}
.dots{position:absolute;left:46px;top:204px;display:flex;gap:4px}
.dots i{width:5px;height:5px;border-radius:50%;background:#fff}
.dots i:first-child{background:#555}
.services{top:310px;height:95px;background:var(--light)}
.service{position:absolute;top:18px;width:100px;text-align:center;font-size:10.5px;color:#444}
.service svg{display:block;margin:0 auto 6px;height:40px}
.service.active{color:var(--orange);font-weight:700}
.h2{font:700 17px/1 "Arimo",sans-serif;color:var(--orange);position:absolute;left:39px}
.who{top:405px;height:131px}
.who p{position:absolute;left:39px;width:600px;font-size:8.6px;line-height:12.5px}
.benefits{top:536px;height:259px;background:var(--light)}
.benefits .intro{position:absolute;left:45px;top:44px;font-size:8.6px}
.card{position:absolute;top:70px;height:161px;background:var(--card)}
.card h3{background:var(--card-head);color:#fff;font-size:10px;font-weight:700;text-align:center;height:32px;display:flex;align-items:center;justify-content:center;line-height:11px}
.card p{padding:10px 6px;text-align:center;font-size:8.6px;line-height:12.3px;color:#555}
.testimonials{top:795px;height:138px}
.quote{position:absolute;top:52px;font-style:italic;font-size:8px;line-height:11px;color:#555}
.quote .mark{position:absolute;left:-24px;top:-4px;font:700 26px/1 Georgia,serif;color:var(--quote-mark)}
.quote .close{display:inline-block;font:700 22px/0 Georgia,serif;color:var(--quote-mark);vertical-align:-10px;margin-left:4px}
.quote .who-said{font-style:normal;font-size:8.6px;color:#444;margin-top:16px}
.divider{position:absolute;top:48px;width:1px;height:80px;background:#e2e2e2}
.clients{top:933px;height:77px;background:#f3f3f3}
.clients h4{position:absolute;left:38px;top:26px;color:var(--orange);font-size:11px;line-height:13px}
.client{position:absolute;top:30px;font-size:15px;font-weight:700;color:#555}
.footer{top:1010px;height:162px;background:var(--footer);color:#fff}
.footer h5{position:absolute;top:16px;font-size:11px;font-weight:700}
.field{position:absolute;left:32px;width:133px;height:18px;background:var(--field);font-style:italic;font-size:8px;padding:4px 8px;color:#fff}
.submit{position:absolute;left:32px;top:135px;width:46px;height:16px;background:var(--orange);font-size:9px;font-weight:700;text-align:center;line-height:16px}
.links{position:absolute;left:184px;top:42px;width:470px;font-size:8.6px;line-height:19.5px}
.links-row{white-space:nowrap}
.links a{color:#fff;text-decoration:none;padding-right:7px;margin-right:6px;border-right:1px solid #666}
.links a:last-child{border:0}
.links a.current{color:var(--orange)}
.copyright{top:1172px;height:28px;background:var(--footer-deep);color:#ddd;text-align:center;font-size:8px;line-height:28px}
</style>
</head>
<body>
<header class="section header">
  <div class="brand"><span class="brand-square"></span>The Mirel Group</div>
  <div class="call">
    <svg width="20" height="20" viewBox="0 0 20 20"><circle cx="10" cy="10" r="9" fill="none" stroke="#222" stroke-width="1.2"/><path d="M7 5c-1 1-1 3 1 6s4 4 5 4l1-1-2-2-1 1c-1-.5-2-2-2.5-3l1-1-1.5-2z" fill="#222"/></svg>
    <div><small>Call Us Today</small><strong>1300 555 014</strong></div>
  </div>
</header>
<nav class="section nav">
  <a class="active" href="#">HOME</a><a href="#">DATA ANALYSIS</a><a href="#">DATA CLEANSING</a><a href="#">DATA MINING</a><a href="#">DATA SCRAPING</a><a href="#">DATA WAREHOUSE</a><a href="#">BLOG</a><a href="#">CONTACT</a>
</nav>
<section class="section hero">
  <div class="hero-photo" role="img" aria-label="Playful photo of a chimp and a child in a colander helmet with goggles beside an old meter"></div>
  <h1>Helping You Creatively<br>Generate Real Value<br>From Your <span>DATA</span></h1>
  <div class="dots"><i></i><i></i><i></i><i></i></div>
</section>
<section class="section services">
  <div class="service active" style="left:38px"><svg viewBox="0 0 40 40" width="40"><g fill="#ff6a00"><rect x="4" y="26" width="5" height="12"/><rect x="11" y="22" width="5" height="16"/><rect x="18" y="18" width="5" height="20"/><rect x="25" y="14" width="5" height="24"/><rect x="32" y="10" width="5" height="28"/></g><polyline points="4,20 12,14 20,16 34,4" fill="none" stroke="#ff6a00" stroke-width="2"/></svg>Data Analysis</div>
  <div class="service" style="left:139px"><svg viewBox="0 0 40 40" width="40"><path d="M34 4 22 20" stroke="#444" stroke-width="3"/><path d="M20 18l6 6-10 12c-4-1-9-5-10-10z" fill="#444"/><g fill="#444"><circle cx="8" cy="8" r="1.5"/><circle cx="14" cy="12" r="1.5"/><circle cx="6" cy="16" r="1.5"/></g></svg>Data Cleansing</div>
  <div class="service" style="left:240px"><svg viewBox="0 0 40 40" width="40"><circle cx="16" cy="16" r="11" fill="none" stroke="#444" stroke-width="3"/><path d="M24 24l11 11" stroke="#444" stroke-width="5"/><path d="M16 10v12M10 16h12" stroke="#444" stroke-width="3"/></svg>Data Mining</div>
  <div class="service" style="left:340px"><svg viewBox="0 0 40 40" width="40"><rect x="3" y="4" width="34" height="24" fill="none" stroke="#444" stroke-width="3"/><path d="M15 32h10l2 4H13z" fill="#444"/><circle cx="20" cy="16" r="4" fill="#444"/><path d="M14 10l12 12M26 10 14 22M20 8v16M12 16h16" stroke="#444" stroke-width="1"/></svg>Data Scraping</div>
  <div class="service" style="left:441px"><svg viewBox="0 0 40 40" width="40"><g fill="#444"><ellipse cx="20" cy="8" rx="14" ry="5"/><path d="M6 11c0 3 6 5 14 5s14-2 14-5v7c0 3-6 5-14 5S6 21 6 18z"/><path d="M6 21c0 3 6 5 14 5s14-2 14-5v8c0 3-6 5-14 5S6 32 6 29z"/></g></svg>Data Warehouse</div>
  <div class="service" style="left:542px"><svg viewBox="0 0 40 40" width="40"><g fill="#fff" stroke="#444" stroke-width="2.5"><rect x="18" y="3" width="16" height="22"/><rect x="12" y="9" width="16" height="22"/><rect x="6" y="15" width="16" height="22"/></g></svg>Data Resources</div>
</section>
<section class="section who">
  <h2 class="h2" style="top:20px">WHO WE ARE</h2>
  <p style="top:45px">The Mirel Group is a Melbourne based business offering a comprehensive range of data services. We specialise in data analysis, data cleansing, data mining, data scraping and data warehouses.</p>
  <p style="top:75px">Our goal is to help you extract value from your data in the form of pragmatic insights, trends and relationships. And then to analyse, interpret and use these findings in innovative ways that empower you to manage your organisation for greater profit, with improved decision-making and enhanced strategic, tactical and operational insight.</p>
</section>
<section class="section benefits">
  <h2 class="h2" style="top:19px">YOUR BENEFITS</h2>
  <p class="intro">Our core speciality is solving business problems that require complex data analysis,cleansing, mining or modelling techniques. Your benefits include:</p>
  <div class="card" style="left:44px;width:139px"><h3>Fast<br>Rate of Income</h3><p>Quick access to skilled data professionals, without the overhead of building and maintaining your own infrastructure and team. Our fees are typically small in contrast to the additional profits or savings that our projects generate for our clients.</p></div>
  <div class="card" style="left:196px;width:138px"><h3>Innovative Practical<br>Solutions</h3><p>We find smart ways to extract useful information from incomplete and disorganised data. We also have extensive industry experience and the quantitative rigour to generate innovative yet pragmatic value-adding solutions.</p></div>
  <div class="card" style="left:347px;width:139px"><h3>Connected To Major<br>Universities</h3><p>We have relationships with leading practitioners at major universities and business schools within Australia. This provides us with ready access to extensive expertise and the latest developments. We have never turned down a project due to it being too complex.</p></div>
  <div class="card" style="left:498px;width:139px"><h3>Always Confidential<br>And Discreet</h3><p>Lorem ipsum dolor sit amet, consectetuer adipiscing elit, sed diam nonummy nibh euismod tincidunt ut laoreet dolore magna aliquam erat volutpat. Ut wisi enim ad minim veniam, quis nostrud exerci tation ullamcorper suscipit lobortis Lorem Ispum is the dummy text.</p></div>
</section>
<section class="section testimonials">
  <h2 class="h2" style="top:20px;left:37px">CLIENT TESTIMONIALS</h2>
  <div class="quote" style="left:61px;width:170px"><span class="mark">&ldquo;</span>Thanks for the fast turnaround on our de-duplication project. ...I'm so impressed that I have already recommended you to two of our suppliers.<span class="close">&rdquo;</span><div class="who-said">RAY T &ndash; Marketing Manager</div></div>
  <div class="divider" style="left:237px"></div>
  <div class="quote" style="left:270px;width:170px"><span class="mark">&ldquo;</span>Thanks for the fast turnaround on our de-duplication project. ...I'm so impressed that I have already recommended you to two of our suppliers.<span class="close">&rdquo;</span><div class="who-said">RAY T &ndash; Marketing Manager</div></div>
  <div class="divider" style="left:441px"></div>
  <div class="quote" style="left:476px;width:175px"><span class="mark">&ldquo;</span>Thanks for your work with our data, it certainly looks and feels clean.<span class="close">&rdquo;</span><div class="who-said">TESSA M &ndash; Marketing Officer</div></div>
</section>
<section class="section clients">
  <h4>SOME PEOPLE<br>WE WORK WITH</h4>
  <div class="client" style="left:155px">Korvel Pharma</div>
  <div class="client" style="left:335px">Nestrin</div>
  <div class="client" style="left:448px">Alderway Labs</div>
  <div class="client" style="left:580px">Hollis Care</div>
</section>
<footer class="section footer">
  <h5 style="left:32px">Quick Inquiry</h5>
  <div class="field" style="top:40px">Name</div>
  <div class="field" style="top:62px">Email</div>
  <div class="field" style="top:84px;height:48px">Message</div>
  <div class="submit">Submit</div>
  <h5 style="left:184px">Quick links</h5>
  <div class="links">
    <div class="links-row"><a href="#">Algorithm Creation</a><a href="#">Cleansing Vantora CRM Data</a><a href="#">Customer Analysis</a><a href="#">Data Analysis</a><a href="#">Data Checking</a></div>
    <div class="links-row"><a href="#">Data Analysis Methods</a><a href="#">Data Cleansing</a><a href="#">Data Deduplication</a><a href="#">Data Management</a><a href="#">Data Merging</a></div>
    <div class="links-row"><a href="#">Data Migration</a><a href="#">Data Mining</a><a href="#">Data Scraping</a><a href="#">Data Verification</a><a href="#">Data Warehouse</a><a href="#">Text Analysis</a></div>
    <div class="links-row"><a href="#">Data Warehouse Methodology</a><a href="#">Financial Analysis</a><a href="#">Procurement Analysis</a><a href="#">Orvix Report Writing</a><a href="#">Blog</a></div>
    <div class="links-row"><a href="#">Contact Us</a><a href="#">Comments Policy</a><a class="current" href="#">Home</a></div>
  </div>
</footer>
<div class="section copyright">Copyright &copy;2014, The Mirel Group is a division of Keelan Holdings (Australia) Pty Ltd. | ABN: 12345678901</div>
</body>
</html>
```